Homebuilder & Remodeling Firm looking for archectrual looking website

We are a Custom home building & remodeling company since 1986 and would like to launch a website.Carl Tondevik the principle of the firm is a graduate of Harwell Univesity school of architecture and draws his own designs and working drawings. and has done many residential, single and multi family projects in the Dallas Ft Worth Metroplex. We want our website to be architectural in design and visually appealing. We will eventually have photos to provide for you. The message we want to communicate is we have current update knowledge with trends, and longevity in experience. Our message is that we are a firm that designs and remodels fully through and we provide a well executed custom home that is unique to each client. The Homes that we build are unique ,authentic and sustainable architectural styles such as mid century modern, contemporary, transitional and they are sophisticated homes to compliment individual lifestyles of our clients. We have a passion for construction and an attention to detail that makes your dreams come to life. We listen to each clients every need in functionality and form and take them from pre-construction to post-construction follow -up.
We help you invest in your home. Thoughts Create Reality

EXAMPLES OF WEBSITES THAT WE LIKE. PLEASE DO
MORE CONTEMPORARY, SLEEK, ARCHITECTURAL

* Please make the LOGO a bigger part of design

http://pellamcrew.build/
https://www.vintrasol.co/
http://dostavanehomes.com/
http://www.milesfardowdesign.com/
http://www.quillmerton.com/
http://fennikdesignstudios.com/about
http://brandelorgc.com/

thank you,

Reason: We have many clients asking to see our website and re ready to launch something for them to look at

Target Market(s)

Home owners, home buyers, interior designers, All ages

Industry/Entity Type

Builders

Coding

Coded - Design and coding required

Number of Pages Required

5+ page

Font styles to use
Sans Serif

Requirements
Must have
• HTML5 OR PHP
• graphic artist must speak English:
• *Visually appealing, user friendly,
• * the website should reflect the stability and integrity of the company since it has been in business for over 30 years
• * a sophistication and refinement is our mandate.
Should not have
• Too busy, too much going on, we want more minimal in design and artsitic

```html
<!DOCTYPE html>
<html lang="en">
<head>
<meta charset="utf-8">
<title>Tondevik Development — Custom Homes &amp; Remodeling</title>
<link href="https://fonts.googleapis.com/css2?family=Alegreya+Sans+SC:wght@300;400;500&family=Questrial&display=swap" rel="stylesheet">
<style>
  :root{
    --navy:#1c2a58;
    --navy-deep:#17234a;
    --ink:#2f3345;
    --text:#5d6070;
    --grey-bg:#eeeeee;
    --card-bg:#f1f1f1;
    --white:#ffffff;
    --muted:#b9b9b9;
  }
  *{box-sizing:border-box;margin:0;padding:0}
  html,body{width:1200px;height:3666px;overflow:hidden}
  body{position:relative;background:var(--white);font-family:"Questrial",Arial,sans-serif;color:var(--text)}
  .sc{font-family:"Alegreya Sans SC","Questrial",sans-serif}
  section,header,footer{position:absolute;left:0;width:1200px}

  /* header */
  .site-header{top:0;height:112px;background:var(--white);border-top:5px solid var(--navy)}
  .brand{position:absolute;left:82px;top:38px;display:flex;align-items:center;gap:12px}
  .brand-square{width:30px;height:30px;background:var(--navy)}
  .brand-name{font-size:27px;color:var(--navy);line-height:1}
  .main-nav{position:absolute;left:433px;top:-5px;height:117px;display:flex;align-items:center}
  .main-nav a{font-size:15px;color:var(--ink);text-decoration:none;padding:0 17px;height:117px;display:flex;align-items:center;letter-spacing:.3px}
  .main-nav a.active{background:var(--navy);color:var(--white);width:92px;justify-content:center;padding:0}
  .nav-search{margin-left:10px}

  /* hero */
  .hero{top:112px;height:568px;background:linear-gradient(100deg,#d8d7d2 0%,#b9b8b3 30%,#2a2c36 45%,#8f8e8b 60%,#e9e7e1 85%,#bdbbb6 100%)}
  .hero-photo{position:absolute;inset:0}
  .hero-caption{position:absolute;left:460px;top:225px;width:676px;height:181px;background:rgba(28,42,88,.78);padding:28px 40px 0 0;text-align:right;color:var(--white)}
  .hero-caption h1{font-family:"Questrial",sans-serif;font-weight:400;font-size:50px;letter-spacing:1px;line-height:1}
  .hero-caption p{font-size:16px;line-height:26px;margin-top:14px;color:#dfe2ee}
  .hero-arrow{position:absolute;top:270px}
  .hero-arrow.prev{left:26px}
  .hero-arrow.next{right:26px}

  /* welcome */
  .welcome{top:680px;height:566px;text-align:center}
  .section-title{font-size:46px;font-weight:400;color:var(--ink);letter-spacing:.5px;line-height:1}
  .section-title b{font-weight:500;color:var(--navy)}
  .welcome .section-title{margin-top:57px}
  .lead{font-size:14px;line-height:24px;color:var(--text);width:1050px;margin:22px auto 0}
  .service-card{position:absolute;top:263px;width:509px;height:237px}
  .service-card.building{left:78px;background:linear-gradient(135deg,#4c556f,#6d7488 50%,#3f4760)}
  .service-card.remodel{left:613px;background:linear-gradient(135deg,#e7e5e1,#c9c6c0 55%,#7d6a5c)}
  .service-card::after{content:"";position:absolute;inset:12px;border:1.5px solid rgba(255,255,255,.75)}
  .service-card span{position:absolute;left:0;right:0;top:98px;font-size:34px;color:var(--white);z-index:1}

  /* about */
  .about{top:1246px;height:411px;background:var(--grey-bg)}
  .about-mark{position:absolute;left:160px;top:55px;width:232px;height:310px;display:flex;flex-direction:column;align-items:center;justify-content:center;gap:22px}
  .about-mark .big-square{width:150px;height:150px;background:var(--navy)}
  .about-mark .big-name{font-size:30px;color:var(--navy);text-align:center;line-height:1.1}
  .about-body{position:absolute;left:486px;top:82px;width:640px}
  .about-body .section-title{font-size:40px}
  .about-body p{font-size:14px;line-height:25px;margin-top:20px;color:var(--text)}
  .btn-more{display:inline-flex;align-items:center;justify-content:center;width:189px;height:52px;background:var(--navy);color:var(--white);font-size:18px;margin-top:20px;letter-spacing:.5px}

  /* dreams */
  .dreams{top:1657px;height:323px;background:linear-gradient(180deg,#2a3c6b 0%,#20305d 55%,#1b2a52 100%);text-align:center;color:var(--white)}
  .dreams .section-title{color:var(--white);font-size:42px;margin-top:70px}
  .dreams .section-title b{color:var(--white)}
  .dreams p{font-size:14px;margin-top:18px;color:#dde1ee}
  .dreams p.tagline{font-style:italic;font-size:16px;margin-top:12px}
  .lead-form{position:absolute;top:210px;left:98px;display:flex;gap:12px}
  .lead-form span{width:260px;height:49px;background:#d9d9d9;color:#6d6d6d;font-style:italic;font-size:13px;text-align:left;padding:16px 14px}
  .lead-form .submit{width:188px;height:49px;border:1.5px solid var(--white);color:var(--white);font-size:19px;display:flex;align-items:center;justify-content:center;margin-left:-2px}

  /* projects */
  .projects{top:1980px;height:689px;text-align:center}
  .projects .section-title{margin-top:70px;font-size:44px}
  .projects .lead{width:900px;margin-top:18px}
  .project-grid{position:absolute;top:203px;left:0;width:1200px;display:grid;grid-template-columns:repeat(4,300px);grid-template-rows:207px 210px}
  .tile{position:relative}
  .t1{background:linear-gradient(160deg,#9fb0b8,#5e6e63 60%,#3f5a35)}
  .t2{background:linear-gradient(160deg,#d9d3c9,#8a5d3e 55%,#3a2a22)}
  .t3{background:var(--navy);border:4px solid var(--white);outline:2px solid var(--navy);outline-offset:-10px;color:var(--white);display:flex;flex-direction:column;justify-content:center}
  .t3 small{font-size:15px;color:#cfd5e6}
  .t3 strong{font-weight:400;font-size:25px;margin-top:10px}
  .t4{background:linear-gradient(170deg,#d6dbe0,#9a928a 55%,#5b5750)}
  .t5{background:linear-gradient(150deg,#c9b9a4,#8c6e50 55%,#4a3a2d)}
  .t6{background:linear-gradient(160deg,#eeeae4,#c8c3bb 55%,#5c4a3b)}
  .t7{background:linear-gradient(120deg,#c7c6c2,#1f2434 50%,#a7a59f)}
  .t8{background:linear-gradient(170deg,#d6dde6,#8e7c6a 55%,#3c3430)}
  .view-all{position:absolute;left:0;top:620px;width:1200px;height:69px;background:var(--navy);color:var(--white);font-size:19px;display:flex;align-items:center;justify-content:center;gap:14px;letter-spacing:.5px}

  /* blog */
  .blog{top:2669px;height:606px;text-align:center}
  .blog .section-title{margin-top:70px;font-size:44px}
  .post{position:absolute;top:132px;width:333px;height:415px;background:var(--card-bg);text-align:left}
  .post.p1{left:78px}.post.p2{left:433px}.post.p3{left:789px}
  .post-photo{height:181px}
  .p1 .post-photo{background:linear-gradient(120deg,#cfcdc8,#1f2535 50%,#bdbab3)}
  .p2 .post-photo{background:linear-gradient(170deg,#3a5f95,#6b84a8 45%,#c9a56d 75%,#5a4a3c)}
  .p3 .post-photo{background:linear-gradient(160deg,#e2ded7,#a08a72 55%,#5a4a3e)}
  .post-meta{height:39px;background:var(--navy);color:var(--white);font-size:14px;display:flex;align-items:center;justify-content:space-between;padding:0 14px}
  .post-meta span{display:flex;align-items:center;gap:8px}
  .post h3{font-family:"Alegreya Sans SC",sans-serif;font-weight:500;font-size:19px;color:var(--navy);line-height:29px;padding:14px 14px 0}
  .post p{font-size:13.5px;line-height:24px;padding:8px 14px 0;color:var(--text)}

  /* footer */
  .site-footer{top:3275px;height:391px;background:linear-gradient(180deg,var(--navy-deep),var(--navy));text-align:center;color:var(--white)}
  .footer-brand{margin-top:61px;display:flex;flex-direction:column;align-items:center;gap:14px}
  .footer-brand .brand-square{width:64px;height:64px;background:var(--white)}
  .footer-brand .brand-name{color:var(--white);font-size:26px}
  .social{display:flex;justify-content:center;gap:10px;margin-top:26px}
  .social span{width:42px;height:42px;border:2px solid var(--white);border-radius:50%}
  .footer-nav{margin-top:18px;font-size:15px;display:flex;justify-content:center;gap:24px}
  .footer-nav a{color:#dfe3ef;text-decoration:none}
  .copyright{margin-top:12px;font-size:14px;color:#dfe3ef}
</style>
</head>
<body>

<header class="site-header">
  <div class="brand"><span class="brand-square"></span><span class="brand-name sc">Tondevik Development</span></div>
  <nav class="main-nav">
    <a class="active" href="#">HOME</a>
    <a href="#">ABOUT US</a>
    <a href="#">SERVICES</a>
    <a href="#">PROJECTS</a>
    <a href="#">BLOG</a>
    <a href="#">CONTACT US</a>
    <svg class="nav-search" width="20" height="20" viewBox="0 0 20 20"><circle cx="8" cy="8" r="6" fill="none" stroke="#1c2a58" stroke-width="2.6"/><line x1="12.5" y1="12.5" x2="18" y2="18" stroke="#1c2a58" stroke-width="3" stroke-linecap="round"/></svg>
  </nav>
</header>

<section class="hero">
  <div class="hero-photo" role="img" aria-label="Photo of a bright modern living room with a dark feature wall, white floor and a low black bench"></div>
  <svg class="hero-arrow prev" width="20" height="50" viewBox="0 0 20 50"><polyline points="17,3 3,25 17,47" fill="none" stroke="#fff" stroke-width="2" opacity=".8"/></svg>
  <svg class="hero-arrow next" width="20" height="50" viewBox="0 0 20 50"><polyline points="3,3 17,25 3,47" fill="none" stroke="#fff" stroke-width="2" opacity=".8"/></svg>
  <div class="hero-caption">
    <h1>RENOVATE YOUR HOME</h1>
    <p>We are a firm that designs and remodels fully through and we provide a<br>well-executed custom home that is unique to each client</p>
  </div>
</section>

<section class="welcome">
  <h2 class="section-title sc">Welcome To <b>Tondevik Development</b></h2>
  <p class="lead">Lorem Ipsum is simply dummy text of the printing and typesetting industry. Lorem Ipsum has been the industry's standard dummy text ever since the 1500s, when an unknown printer took a galley of type. It has survived not only five centuries, but also the leap into electronic typesetting, remaining essentially unchanged. It was popularised in the 1960s with the release of Letraset sheets containing Lorem Ipsum passages, and more recently .</p>
  <div class="service-card building" role="img" aria-label="Photo of a modern home interior with a floating staircase"><span class="sc">Home Building</span></div>
  <div class="service-card remodel" role="img" aria-label="Photo of a couple looking over a sketched room plan"><span class="sc">Remodeling</span></div>
</section>

<section class="about">
  <div class="about-mark"><span class="big-square"></span><span class="big-name sc">Tondevik<br>Development</span></div>
  <div class="about-body">
    <h2 class="section-title sc">About <b>Tondevik Development</b></h2>
    <p>Lorem Ipsum is simply dummy text of the printing and typesetting industry. Lorem Ipsum has been the industry's standard dummy text ever since the 1500s, when an unknown printer took a galley of type. It has survived not only five centuries, but also the leap into electronic typesetting, remaining essentially unchanged. It was popularised in the 1960s with the release of Letraset sheets containing.</p>
    <span class="btn-more">KNOW MORE</span>
  </div>
</section>

<section class="dreams" role="img" aria-label="Dusk photo of a modern house under a deep blue sky">
  <h2 class="section-title sc">Your Dreams <b>Come To Life</b></h2>
  <p>We listen to each client every need in functionality and form and take them from pre, post-construction follow -up.</p>
  <p class="tagline">We help you invest in your home. Thoughts Create Reality</p>
  <div class="lead-form">
    <span>Name*</span><span>Email*</span><span>Your Requirement*</span>
    <span class="submit">SUBMIT</span>
  </div>
</section>

<section class="projects">
  <h2 class="section-title sc">Our <b>Projects</b></h2>
  <p class="lead">Lorem Ipsum is simply dummy text of the printing and typesetting industry. Lorem Ipsum has been the industry's standard dummy text ever since, when an unknown printer took a galley .</p>
  <div class="project-grid">
    <div class="tile t1" role="img" aria-label="Photo of a curved modern house with a lawn and lounge chairs"></div>
    <div class="tile t2" role="img" aria-label="Photo of a timber-lined modern terrace at night"></div>
    <div class="tile t3"><small class="sc">Project title</small><strong class="sc">Lorem is simply text</strong></div>
    <div class="tile t4" role="img" aria-label="Photo of a flat-roofed modern house front"></div>
    <div class="tile t5" role="img" aria-label="Photo of a wooden kitchen with open shelving"></div>
    <div class="tile t6" role="img" aria-label="Photo of a bright living room with armchairs"></div>
    <div class="tile t7" role="img" aria-label="Photo of an interior with a dark feature wall"></div>
    <div class="tile t8" role="img" aria-label="Photo of a multi-level modern house at dusk"></div>
  </div>
  <div class="view-all">VIEW ALL
    <svg width="26" height="14" viewBox="0 0 26 14"><line x1="1" y1="7" x2="24" y2="7" stroke="#fff" stroke-width="2"/><polyline points="18,1 24,7 18,13" fill="none" stroke="#fff" stroke-width="2"/></svg>
  </div>
</section>

<section class="blog">
  <h2 class="section-title sc">Latest <b>Blog</b></h2>

  <article class="post p1">
    <div class="post-photo" role="img" aria-label="Photo of a modern interior with a dark wall"></div>
    <div class="post-meta">
      <span><svg width="14" height="14" viewBox="0 0 14 14"><rect x="1" y="2" width="12" height="11" fill="none" stroke="#fff" stroke-width="1.5"/><line x1="1" y1="5.5" x2="13" y2="5.5" stroke="#fff" stroke-width="1.5"/></svg>18 Feb 2017</span>
      <span><svg width="16" height="14" viewBox="0 0 16 14"><ellipse cx="8" cy="6" rx="7" ry="5" fill="#fff"/><polygon points="3,9 2,13 7,10" fill="#fff"/></svg>3 Comment</span>
    </div>
    <h3>Lorem ipsum is Simple Dummy<br>Text Of Print And Type</h3>
    <p>Lorem Ipsum is simply dummy text of the printing and typesetting industry. Lorem Ipsum has been the industry's.</p>
  </article>

  <article class="post p2">
    <div class="post-photo" role="img" aria-label="Photo of a glass-walled modern house at twilight"></div>
    <div class="post-meta">
      <span><svg width="14" height="14" viewBox="0 0 14 14"><rect x="1" y="2" width="12" height="11" fill="none" stroke="#fff" stroke-width="1.5"/><line x1="1" y1="5.5" x2="13" y2="5.5" stroke="#fff" stroke-width="1.5"/></svg>18 Feb 2017</span>
      <span><svg width="16" height="14" viewBox="0 0 16 14"><ellipse cx="8" cy="6" rx="7" ry="5" fill="#fff"/><polygon points="3,9 2,13 7,10" fill="#fff"/></svg>3 Comment</span>
    </div>
    <h3>Lorem ipsum is Simple Dummy<br>Text Of Print And Type</h3>
    <p>Lorem Ipsum is simply dummy text of the printing and typesetting industry. Lorem Ipsum has been the industry's.</p>
  </article>

  <article class="post p3">
    <div class="post-photo" role="img" aria-label="Photo of a warm-toned open kitchen"></div>
    <div class="post-meta">
      <span><svg width="14" height="14" viewBox="0 0 14 14"><rect x="1" y="2" width="12" height="11" fill="none" stroke="#fff" stroke-width="1.5"/><line x1="1" y1="5.5" x2="13" y2="5.5" stroke="#fff" stroke-width="1.5"/></svg>18 Feb 2017</span>
      <span><svg width="16" height="14" viewBox="0 0 16 14"><ellipse cx="8" cy="6" rx="7" ry="5" fill="#fff"/><polygon points="3,9 2,13 7,10" fill="#fff"/></svg>3 Comment</span>
    </div>
    <h3>Lorem ipsum is Simple Dummy<br>Text Of Print And Type</h3>
    <p>Lorem Ipsum is simply dummy text of the printing and typesetting industry. Lorem Ipsum has been the industry's.</p>
  </article>
</section>

<footer class="site-footer">
  <div class="footer-brand"><span class="brand-square"></span><span class="brand-name sc">Tondevik Development</span></div>
  <div class="social"><span></span><span></span><span></span></div>
  <nav class="footer-nav">
    <a href="#">Home</a><a href="#">About Us</a><a href="#">Services</a><a href="#">Projects</a><a href="#">Blog</a><a href="#">Contact</a>
  </nav>
  <p class="copyright">©Tondevik Development - 2017. All Rights Reserved</p>
</footer>

</body>
</html>
```